Design a Unique and Eye-Catching Necklace Card for Verandelle's New Lumenwave Line

Attention all creative minds from around the world! Verandelle, a company known for its free-spirited and bohemian chic vibe, is proud to announce a new design contest. We are inviting you to create a dynamic and unique necklace card for our upcoming Lumenwave line.

Our new Lumenwave line comprises 12-20 unique necklace combinations. Each necklace features different stones, each with its own healing properties and associated zodiac sign. We are looking for a template that can be easily modified to change the names of the stones, zodiac sign, and the colors to match the specific stones on each necklace.

The card should be 3 x 4,
It should include the names of the stones, the associated zodiac sign (if applicable), a few words about the healing properties of the stones, and a captivating graphic that represents the colors of the stones.

Our goal is to delight our customers with packaging as unique as the necklaces themselves. The necklace should be the focal point, but the text and graphic on the card should also draw the eye.

Please note that our target audience includes mid-priced boutiques across the country and festival-goers in Colorado. Your design should reflect the unique taste and free spirit of our clientele.

We are excited to see your creativity shine in this project. If there are any points that need clarification, please do not hesitate to ask. We look forward to your participation in bringing the Lumenwave line to life!
https://www.plorvex.example/board/QKTm_ZRwpe/u3hb9XKdLqWm72RtPoaVnc/edit?ref=QKTm_ZRwpe&src=share

https://www.plorvex.example/board/QKTr_BNyhwa/t8Ld-WsPzMEY246VqoXjNd/edit?ref=QKTr_BNyhwa&src=share
I want to use the flowing watercolor and have it change with each necklace color.
Use the necklaces below. Incorporate the zodiac symbol as is shown below.

Examples of other cards in our collection

The Little Pebble Pendant: https://www.plorvex.example/board/QKTh_WomRtc/pbMRx63CKqnYs905Bd-aLe/edit?ref=QKTh_WomRtc&src=share

Other examples of necklace cards I like:

https://www.tindramart.example/item/731920584/green-emerald-stone-necklace-emerald?k=a1b2c3d4e5f60718293a4b5c6d7e8f9012345678&s=7d3e91ab

https://www.tindramart.example/item/846201937/january-birthstone-necklace-green-garnet?k=b2c3d4e5f60718293a4b5c6d7e8f901234567890&s=4c82fe10

https://www.tindramart.example/item/2093748165/natural-crystal-bracelets-empath?k=c3d4e5f60718293a4b5c6d7e8f90123456789012&s=9ab0c37d

https://www.tindramart.example/item/2174603958/black-obsidian-protection-necklace-black?k=d4e5f60718293a4b5c6d7e8f9012345678901234&s=e15d6b28

Target Market(s)

Women aged 25-50 with a spiritual, hippy, bohemain, yoga vibe.

Industry/Entity Type

Handmade Jewelry | Wholesale jewelry | Retail Jewelry sales at Festivals

Font styles to use
Script

Colors

Designer to choose colors to be used in the design.

Requirements
Must have
• A template that can be interchangable with the stone colors, names and healing properties.
Nice to have
• Some different ideas about the graphic color patterns on the card.
Should not have
• Any graphic that would cover the middle of the necklace card and keep people from seeing the neckalce

```html
<!DOCTYPE html>
<html lang="en">
<head>
<meta charset="utf-8">
<title>Lumenwave Necklace Cards</title>
<link href="https://fonts.googleapis.com/css2?family=Cinzel:wght@400&family=Outfit:wght@300;400&display=swap" rel="stylesheet">
<style>
  :root {
    --page: #ffffff;
    --aqua-ink: #1d4fc6;
    --aqua-bg-top: #f7f9fe;
    --aqua-bg-bottom: #eef2fb;
    --chryso-ink: #4bada3;
    --chryso-bg-top: #f6f8f7;
    --chryso-bg-bottom: #eef1f0;
    --fluor-ink: #a24c9f;
    --fluor-bg-top: #fbfbfc;
    --fluor-bg-bottom: #f1f1f3;
    --jasper-ink: #2d6a56;
    --jasper-bg: #ffffff;
    --chain: #c4c8cc;
  }
  * { margin: 0; padding: 0; box-sizing: border-box; }
  html, body {
    width: 1200px; height: 304px; overflow: hidden;
    background: var(--page);
  }
  .card-row { position: relative; width: 1200px; height: 304px; }
  .card {
    position: absolute; top: 6px; width: 292px; height: 292px;
    overflow: hidden; text-align: center;
  }
  .card--aquamarine { left: 7px; color: var(--aqua-ink);
    background: linear-gradient(180deg, var(--aqua-bg-top), var(--aqua-bg-bottom)); }
  .card--chrysocolla { left: 307px; color: var(--chryso-ink);
    background: linear-gradient(180deg, var(--chryso-bg-top), var(--chryso-bg-bottom)); }
  .card--fluorite { left: 609px; color: var(--fluor-ink);
    background: linear-gradient(180deg, var(--fluor-bg-top), var(--fluor-bg-bottom)); }
  .card--ocean-jasper { left: 907px; color: var(--jasper-ink); background: var(--jasper-bg); }

  .necklace { position: absolute; left: 0; top: 0; width: 292px; height: 292px; }
  .stone-name {
    position: absolute; left: 0; right: 0; top: 28px;
    font-family: "Cinzel", serif; font-weight: 400;
    font-size: 27px; line-height: 28px; letter-spacing: -0.3px;
  }
  .healing {
    position: absolute; left: 0; right: 0; top: 195px;
    font-family: "Outfit", sans-serif; font-weight: 300;
    font-size: 14.5px; line-height: 15px;
  }
  .healing--two-line { top: 188px; }
  .zodiac {
    position: absolute; left: 0; right: 0; top: 239px;
    display: flex; flex-direction: column; align-items: center;
  }
  .zodiac-name {
    font-family: "Outfit", sans-serif; font-weight: 400;
    font-size: 7.5px; letter-spacing: 1.6px; line-height: 9px;
  }
  .zodiac-badge {
    margin-top: 4px; width: 29px; height: 29px; border-radius: 50%;
    background: currentColor; display: flex; align-items: center; justify-content: center;
  }
  .zodiac-glyph-text {
    color: #fff; font-family: "Outfit", sans-serif; font-size: 17px; line-height: 1;
  }
</style>
</head>
<body>
<div class="card-row">

  <section class="card card--aquamarine">
    <svg class="necklace" viewBox="0 0 292 292" role="img" aria-label="Photo of an aquamarine and kyanite bead necklace on a silver chain">
      <defs>
        <linearGradient id="beads-aqua" x1="0" x2="1">
          <stop offset="0" stop-color="#3f7fe0"/><stop offset="0.3" stop-color="#8fb3d8"/>
          <stop offset="0.5" stop-color="#b9cde0"/><stop offset="0.7" stop-color="#6f9fd8"/>
          <stop offset="1" stop-color="#3a78dc"/>
        </linearGradient>
      </defs>
      <path d="M4 76 Q146 180 288 76" fill="none" stroke="var(--chain)" stroke-width="1"/>
      <path d="M28 103 Q146 178 264 103" fill="none" stroke="url(#beads-aqua)" stroke-width="14" stroke-linecap="round"/>
    </svg>
    <h2 class="stone-name">Aquamarine<br>&amp; Kyanite</h2>
    <p class="healing">Reduce Stress &amp; Anxiety</p>
    <div class="zodiac">
      <span class="zodiac-name">PISCES</span>
      <span class="zodiac-badge">
        <svg width="15" height="15" viewBox="0 0 15 15" fill="none" stroke="#fff" stroke-width="1.8" stroke-linecap="round">
          <path d="M2 2.5 Q7.5 4.5 13 2.5"/><path d="M2 12.5 Q7.5 10.5 13 12.5"/>
          <path d="M5 3.6 V11.4"/><path d="M10 3.6 V11.4"/>
        </svg>
      </span>
    </div>
  </section>

  <section class="card card--chrysocolla">
    <svg class="necklace" viewBox="0 0 292 292" role="img" aria-label="Photo of a chrysocolla and aquamarine bead necklace on a silver chain">
      <defs>
        <linearGradient id="beads-chryso" x1="0" x2="1">
          <stop offset="0" stop-color="#1f6d6a"/><stop offset="0.2" stop-color="#b9dccd"/>
          <stop offset="0.45" stop-color="#2f7f80"/><stop offset="0.6" stop-color="#1e3d40"/>
          <stop offset="0.85" stop-color="#5f8b86"/><stop offset="1" stop-color="#c9e1d4"/>
        </linearGradient>
      </defs>
      <path d="M0 70 Q146 200 292 76" fill="none" stroke="var(--chain)" stroke-width="1"/>
      <path d="M34 100 Q146 192 262 105" fill="none" stroke="url(#beads-chryso)" stroke-width="16" stroke-linecap="round"/>
    </svg>
    <h2 class="stone-name">Chrysocolla<br>&amp; Aquamarine</h2>
    <p class="healing healing--two-line">Detoxifies the liver,<br>kidneys, and intestines.</p>
    <div class="zodiac">
      <span class="zodiac-name">VIRGO</span>
      <span class="zodiac-badge"><span class="zodiac-glyph-text">♍&#xFE0E;</span></span>
    </div>
  </section>

  <section class="card card--fluorite">
    <svg class="necklace" viewBox="0 0 292 292" role="img" aria-label="Photo of a fluorite bead necklace on a silver chain">
      <defs>
        <linearGradient id="beads-fluor" x1="0" x2="1">
          <stop offset="0" stop-color="#e4d4f2"/><stop offset="0.25" stop-color="#c29bd6"/>
          <stop offset="0.45" stop-color="#8a2f78"/><stop offset="0.6" stop-color="#a93b8c"/>
          <stop offset="0.8" stop-color="#9e86b8"/><stop offset="1" stop-color="#c9c3d4"/>
        </linearGradient>
      </defs>
      <path d="M0 102 Q146 180 292 94" fill="none" stroke="var(--chain)" stroke-width="1"/>
      <path d="M26 118 Q146 182 266 112" fill="none" stroke="url(#beads-fluor)" stroke-width="13" stroke-linecap="round"/>
    </svg>
    <h2 class="stone-name">Fluorite</h2>
    <p class="healing">Improves decision making</p>
    <div class="zodiac">
      <span class="zodiac-name">PISCES</span>
      <span class="zodiac-badge">
        <svg width="15" height="15" viewBox="0 0 15 15" fill="none" stroke="#fff" stroke-width="1.8" stroke-linecap="round">
          <path d="M2 2.5 Q7.5 4.5 13 2.5"/><path d="M2 12.5 Q7.5 10.5 13 12.5"/>
          <path d="M5 3.6 V11.4"/><path d="M10 3.6 V11.4"/>
        </svg>
      </span>
    </div>
  </section>

  <section class="card card--ocean-jasper">
    <svg class="necklace" viewBox="0 0 292 292" role="img" aria-label="Photo of an ocean jasper bead necklace on a silver chain">
      <defs>
        <linearGradient id="beads-jasper" x1="0" x2="1">
          <stop offset="0" stop-color="#6d6a45"/><stop offset="0.25" stop-color="#2f6a5c"/>
          <stop offset="0.45" stop-color="#d8c9aa"/><stop offset="0.6" stop-color="#d07a32"/>
          <stop offset="0.8" stop-color="#8a4a3c"/><stop offset="1" stop-color="#e59aa4"/>
        </linearGradient>
      </defs>
      <path d="M24 2 Q60 180 146 172 Q232 180 280 2" fill="none" stroke="var(--chain)" stroke-width="1"/>
      <path d="M33 70 Q62 172 146 166 Q230 172 262 64" fill="none" stroke="url(#beads-jasper)" stroke-width="17" stroke-linecap="round"/>
    </svg>
    <h2 class="stone-name">Ocean Jasper</h2>
    <p class="healing">Alleviates depression &amp; stress</p>
  </section>

</div>
</body>
</html>
```